Business Coaching Model and Flow Chart

We need this flowchart, attached, to be updated in a modern and engaging way. This flowchart is the cornerstone of a business coaching class we are running, and will be the main support reference for the people who take the class. We are open to ideas as to how it is presented, but we would like a largely minimalist look that leaves space to be impactful where the key information sites. Our colour scheme is primary red (D51C29), white, grey (333333), black, and secondary green (3C8740). We will also need our logo present (attached).

```html
<!DOCTYPE html>
<html lang="en">
<head>
<meta charset="utf-8">
<title>Groups to Teams Through Learning Together</title>
<link rel="stylesheet" href="https://fonts.googleapis.com/css2?family=Roboto+Condensed:ital,wght@0,400;0,500;0,700;1,300&display=swap">
<style>
  :root {
    --red: #d51c29;
    --green: #3c8740;
    --grey: #333333;
    --bg: #f2f2f2;
    --white: #ffffff;
  }
  * { margin: 0; padding: 0; box-sizing: border-box; }
  html, body { width: 1200px; height: 673px; overflow: hidden; background: var(--bg); }
  body { font-family: "Roboto Condensed", "Arial Narrow", sans-serif; color: var(--grey); position: relative; }

  .title {
    position: absolute; left: 16px; top: 27px; width: 489px; height: 44px;
    background: var(--red); color: var(--white); border-radius: 11px;
    font-weight: 700; font-size: 25px; line-height: 44px; text-align: center; letter-spacing: 0.1px;
  }

  .brand { position: absolute; left: 1064px; top: 15px; width: 80px; text-align: center; }
  .brand-dot { display: block; width: 58px; height: 58px; border-radius: 50%; background: var(--red); margin: 0 auto 5px; }
  .brand-name { font-weight: 700; font-size: 8px; color: var(--red); text-transform: uppercase; letter-spacing: 0.3px; }

  .stage {
    position: absolute; top: 100px; width: 154px; height: 50px; border-radius: 11px;
    display: flex; align-items: center; justify-content: center; text-align: center;
    font-weight: 500; font-size: 12.5px; line-height: 15.5px; text-transform: uppercase;
    border: 1px solid var(--grey); background: var(--bg); color: var(--grey);
  }
  .stage--problem { background: var(--red); border-color: var(--red); color: var(--white); }
  .stage--solution { background: var(--green); border-color: var(--green); color: var(--white); }

  .pointer { position: absolute; width: 20px; height: 11px; }

  .panel { position: absolute; top: 189px; width: 154px; background: var(--white); border-radius: 7px; }
  .panel--problem { left: 16px; height: 237px; }
  .panel--solution { left: 1028px; height: 261px; }

  .divider { position: absolute; top: 202px; width: 1px; height: 294px; background: var(--grey); }

  .list { position: absolute; top: 195px; list-style: none; font-size: 12.4px; line-height: 27.9px; font-weight: 500; white-space: nowrap; }
  .list .soft { font-weight: 300; font-style: italic; }
  .list--problem { color: var(--red); font-weight: 700; }
  .list--solution { color: var(--green); font-weight: 700; }

  .base-bar { position: absolute; left: 32px; top: 642px; width: 1150px; height: 13px; background: var(--grey); }
</style>
</head>
<body>
  <h1 class="title">GROUPS to TEAMS Through Learning Together</h1>

  <div class="brand">
    <span class="brand-dot"></span>
    <span class="brand-name">Mara Ellison</span>
  </div>

  <div class="stage stage--problem" style="left:16px">Problem</div>
  <div class="stage" style="left:184px">Clarify Challenges<br>Diagnostics</div>
  <div class="stage" style="left:353px">Planning for Success<br>Make a Plan</div>
  <div class="stage" style="left:522px">Learn the Tools<br>Workshops</div>
  <div class="stage" style="left:690px">Doing<br>Mastering the Tools</div>
  <div class="stage" style="left:859px">Reflect-Adapt<br>Embed</div>
  <div class="stage stage--solution" style="left:1028px">Solution</div>

  <svg class="pointer" style="left:82px;top:150px" viewBox="0 0 20 11"><path d="M0 0h20L10 11z" fill="var(--red)"/></svg>
  <svg class="pointer" style="left:251px;top:150px" viewBox="0 0 20 11"><path d="M0 0h20L10 11z" fill="var(--grey)"/></svg>
  <svg class="pointer" style="left:420px;top:150px" viewBox="0 0 20 11"><path d="M0 0h20L10 11z" fill="var(--grey)"/></svg>
  <svg class="pointer" style="left:590px;top:150px" viewBox="0 0 20 11"><path d="M0 0h20L10 11z" fill="var(--grey)"/></svg>
  <svg class="pointer" style="left:757px;top:150px" viewBox="0 0 20 11"><path d="M0 0h20L10 11z" fill="var(--grey)"/></svg>
  <svg class="pointer" style="left:926px;top:150px" viewBox="0 0 20 11"><path d="M0 0h20L10 11z" fill="var(--grey)"/></svg>
  <svg class="pointer" style="left:1094px;top:152px" viewBox="0 0 20 11"><path d="M0 11h20L10 0z" fill="var(--green)"/></svg>

  <div class="panel panel--problem"></div>
  <div class="panel panel--solution"></div>

  <div class="divider" style="left:177px"></div>
  <div class="divider" style="left:345px"></div>
  <div class="divider" style="left:514px"></div>
  <div class="divider" style="left:683px"></div>
  <div class="divider" style="left:852px"></div>
  <div class="divider" style="left:1017px"></div>

  <ul class="list list--problem" style="left:33px">
    <li>Underbilling</li><li>Staff Retention</li><li>Hard to Recruit</li><li>Client Complaints</li>
    <li>Staff Stress Burnout</li><li>Conflict</li><li>NDIS Constant Change</li><li>Limited in Best Practise</li>
  </ul>

  <ul class="list" style="left:189px">
    <li>Scoping</li><li>Interviews</li><li>Group Reflection</li><li>Opinion Surveys</li><li>Certified Assessments</li>
    <li class="soft">Personality Styles</li><li class="soft">Work Preference</li><li class="soft">Strengths&amp;Values</li>
    <li class="soft">Trust</li><li class="soft">360</li>
  </ul>

  <ul class="list" style="left:358px">
    <li>Team Data Analysis</li><li>Workshop</li><li>Individual Development Plan</li><li>Team Development Plan</li><li>Organisational Plan</li>
  </ul>

  <ul class="list" style="left:526px">
    <li>Foundation Workshops</li><li class="soft">Difficult Conversations</li><li class="soft">Giving&amp;Receiving Feedback</li>
    <li class="soft">Values Alignment</li><li class="soft">Shared Purpose</li><li class="soft">Ways of Working</li>
    <li class="soft">Diversity</li><li class="soft">Wellbeing</li><li class="soft">Time Management</li><li>Customised Workshops</li>
  </ul>

  <ul class="list" style="left:695px">
    <li>Group Coaching</li><li>Team Coaching</li><li>Individual Coaching</li><li>Peer Learning</li><li>Lunch ‘n Learnt</li>
  </ul>

  <ul class="list" style="left:864px">
    <li>Culture Committee</li><li>Embedding Workshop</li><li>Culture Collateral</li><li>WOW Manifesto</li>
    <li>Leadership Team Coaching</li><li>Measure ROI</li><li>Review Success</li><li>Evaluation Surveys</li>
    <li>Temperature Checks</li><li>Recruit to Suit</li><li>Future Proofing - what next?</li>
  </ul>

  <ul class="list list--solution" style="left:1038px">
    <li>Self Awareness&amp;Ownership</li><li>Partnership</li><li>Great Place to Work</li><li>Growth Mindset</li>
    <li>Coach Approach Culture</li><li>Feedback Culture</li><li>Way to Manage Conflict</li><li>Best Practise</li><li>Communication Skills</li>
  </ul>

  <svg style="position:absolute;left:82px;top:462px" width="20" height="160" viewBox="0 0 20 160">
    <g fill="var(--red)">
      <path d="M0 0h20l-10 11z"/><path d="M0 29h20l-10 11z"/><path d="M0 58h20l-10 11z"/>
      <path d="M0 88h20l-10 11z"/><path d="M0 117h20l-10 11z"/><path d="M0 147h20l-10 11z"/>
    </g>
  </svg>

  <svg style="position:absolute;left:1094px;top:491px" width="20" height="130" viewBox="0 0 20 130">
    <g fill="var(--green)">
      <path d="M0 11h20L10 0z"/><path d="M0 40h20L10 29z"/><path d="M0 69h20L10 58z"/>
      <path d="M0 99h20L10 88z"/><path d="M0 128h20L10 117z"/>
    </g>
  </svg>

  <svg class="pointer" style="left:251px;top:600px" viewBox="0 0 20 11"><path d="M0 0h20L10 11z" fill="var(--grey)"/></svg>
  <svg class="pointer" style="left:420px;top:600px" viewBox="0 0 20 11"><path d="M0 0h20L10 11z" fill="var(--grey)"/></svg>
  <svg class="pointer" style="left:590px;top:600px" viewBox="0 0 20 11"><path d="M0 0h20L10 11z" fill="var(--grey)"/></svg>
  <svg class="pointer" style="left:757px;top:600px" viewBox="0 0 20 11"><path d="M0 0h20L10 11z" fill="var(--grey)"/></svg>
  <svg class="pointer" style="left:926px;top:600px" viewBox="0 0 20 11"><path d="M0 0h20L10 11z" fill="var(--grey)"/></svg>

  <div class="base-bar"></div>
</body>
</html>
```